Marketing graphics & images for Shopify store

I need someone to create some graphics/images for a coffee sales shopify storefront incorporating my existing logo and want variations on the logo colour so it blends with background images. Freelancer is to provide suitable coffee product related images and designs. Want a catalogue of images i can rotate and use on the storefront.

The tagline on the storefront page " a fresh start to your day" will change - i will update brief accordingly.

Font styles to use
Script

Requirements
Must have
• A variety of images sizes and graphics to be rotated for website marketing purposes.

Also would like some additional logo files with varying colors - ie black version, white version. Darker more chocolate brown version. Need to be logo quality

```html
<!DOCTYPE html>
<html lang="en">
<head>
<meta charset="utf-8">
<title>Café do Marinheiro – A Fresh Start To Your Day</title>
<link rel="stylesheet" href="https://fonts.googleapis.com/css2?family=Abril+Fatface&family=Oswald:wght@500&display=swap">
<style>
  :root {
    --paper: #f4f4f4;
    --ink: #1e1e1e;
    --roast: #5c1608;
    --crema: #c08a66;
    --espresso: #7a3a1c;
    --porcelain: #ffffff;
  }
  * { margin: 0; padding: 0; box-sizing: border-box; }
  html, body {
    width: 1200px;
    height: 656px;
    overflow: hidden;
    background: var(--paper);
  }
  .banner {
    position: relative;
    width: 1200px;
    height: 656px;
    background: var(--paper);
    overflow: hidden;
    font-family: "Abril Fatface", serif;
    color: var(--ink);
  }
  .coffee-photo {
    position: absolute;
    left: 640px;
    top: 100px;
    width: 560px;
    height: 480px;
    background:
      radial-gradient(ellipse 30% 22% at 82% 28%, var(--porcelain) 0%, rgba(255,255,255,0) 100%),
      radial-gradient(ellipse 34% 16% at 82% 84%, var(--porcelain) 0%, rgba(255,255,255,0) 100%),
      radial-gradient(ellipse 48% 22% at 42% 52%, var(--espresso) 0%, var(--crema) 45%, rgba(244,244,244,0) 100%);
    z-index: 1;
  }
  .brand {
    position: absolute;
    left: 216px;
    top: 140px;
    display: flex;
    align-items: center;
    gap: 12px;
    z-index: 2;
  }
  .brand-mark {
    width: 84px;
    height: 84px;
    border-radius: 50%;
    background: var(--ink);
  }
  .brand-name {
    font-size: 30px;
    line-height: 1;
    color: var(--ink);
  }
  .headline {
    position: absolute;
    z-index: 2;
    line-height: 1;
    color: var(--ink);
  }
  .headline-fresh {
    left: 158px;
    top: 236px;
    font-size: 122px;
  }
  .headline-start {
    left: 304px;
    top: 339px;
    font-size: 122px;
  }
  .headline-day {
    left: 310px;
    top: 444px;
    font-size: 50px;
  }
  .web-ribbon {
    position: absolute;
    left: 0;
    top: 556px;
    width: 424px;
    height: 54px;
    z-index: 2;
  }
  .web-ribbon svg { position: absolute; inset: 0; }
  .web-address {
    position: absolute;
    left: 46px;
    top: 0;
    height: 54px;
    line-height: 54px;
    font-family: "Oswald", sans-serif;
    font-weight: 500;
    font-size: 27px;
    letter-spacing: 0.5px;
    color: var(--porcelain);
  }
</style>
</head>
<body>
  <main class="banner">
    <div class="coffee-photo" role="img" aria-label="White coffee cup tipping over with a splash of coffee, a saucer and a spoon falling beside it"></div>

    <div class="brand">
      <span class="brand-mark"></span>
      <span class="brand-name">Café do Marinheiro</span>
    </div>

    <h1>
      <span class="headline headline-fresh">A Fresh</span>
      <span class="headline headline-start">Start</span>
      <span class="headline headline-day">To Your Day</span>
    </h1>

    <div class="web-ribbon">
      <svg width="424" height="54" viewBox="0 0 424 54" aria-hidden="true">
        <polygon points="0,0 397,0 424,54 0,54" fill="var(--roast)"/>
      </svg>
      <span class="web-address">WWW.CAFEDOMARINHEIRO.COM</span>
    </div>
  </main>
</body>
</html>
```